Real estate business card

I need a business card for my real estate company. I help clients buy and sell properties. I would like to keep the design very simple and professional. I would like the design to convey professionalism, safety and trust. I prefer no graphics but a simple logo design would be nice if that is part of what you do.
Updates

Please keep the designs simple. No high-rise buildings please. 

Reason: My design has not been finalized.

Target Market(s)

Age group 30-60 mostly affluent

Industry/Entity Type

Real Estate

Contact Information for Business Card

Velmont Realtors
Howard Prisk, Broker
4153 Marlow Ave. #226, La Crescenta, CA 91207

Requirements
Nice to have
• Logo can be combination of my initials HP or just Z or a simple geometric shape? Please see "Desig Ideas" attachment. No pics of houses or shaking hands, dollar bills, $, %, etc...
Please use fonts similar to Helvetica for a clean, modern look (think Northern European design, simple, clean yet bold)

Also use font colors such as blue, grey in different shades. Use pastel colors if better.

```html
<!DOCTYPE html>
<html lang="en">
<head>
<meta charset="utf-8">
<title>Velmont Realtors – Business Card</title>
<link rel="stylesheet" href="https://fonts.googleapis.com/css2?family=Arimo:wght@400&display=swap">
<style>
  :root {
    --card-bg: #000000;
    --brand-blue: #2b9fdc;
    --detail-blue: #4b93cc;
  }
  html, body {
    margin: 0;
    padding: 0;
    width: 1200px;
    height: 702px;
    overflow: hidden;
    background: var(--card-bg);
  }
  .card {
    position: relative;
    width: 1200px;
    height: 702px;
    background: var(--card-bg);
    font-family: "Arimo", "Helvetica Neue", Helvetica, Arial, sans-serif;
    font-weight: 400;
    color: var(--brand-blue);
  }
  .brand {
    position: absolute;
    left: 60px;
    top: 0;
    width: 530px;
    height: 702px;
    text-align: center;
  }
  .brand-square {
    position: absolute;
    left: 218px;
    top: 228px;
    width: 110px;
    height: 110px;
    box-sizing: border-box;
    border: 8px solid var(--brand-blue);
    border-radius: 4px;
  }
  .brand-name {
    position: absolute;
    left: 0;
    width: 100%;
    top: 386px;
    margin: 0;
    font-size: 56px;
    line-height: 1;
    letter-spacing: 0.42em;
    text-indent: 0.42em;
    font-weight: 400;
    color: var(--brand-blue);
  }
  .brand-sub {
    position: absolute;
    left: 0;
    width: 100%;
    top: 465px;
    margin: 0;
    font-size: 19px;
    line-height: 1;
    letter-spacing: 1.05em;
    text-indent: 1.05em;
    font-weight: 400;
    color: var(--brand-blue);
  }
  .divider {
    position: absolute;
    left: 598px;
    top: 118px;
    width: 4px;
    height: 460px;
    background: var(--brand-blue);
  }
  .contact {
    position: absolute;
    left: 689px;
    top: 0;
    width: 500px;
  }
  .contact-name {
    position: absolute;
    top: 136px;
    margin: 0;
    font-size: 45px;
    line-height: 1;
    letter-spacing: 0.04em;
    white-space: nowrap;
    font-weight: 400;
    color: var(--brand-blue);
  }
  .contact-title {
    position: absolute;
    top: 198px;
    margin: 0;
    font-size: 16px;
    line-height: 1;
    letter-spacing: 0.72em;
    color: var(--brand-blue);
  }
  .detail {
    position: absolute;
    margin: 0;
    font-size: 28px;
    line-height: 1;
    white-space: nowrap;
    color: var(--detail-blue);
  }
  .detail-label {
    display: inline-block;
    width: 131px;
  }
  .phone   { top: 253px; }
  .fax     { top: 288px; }
  .email   { top: 342px; }
  .license { top: 395px; }
  .address { top: 454px; line-height: 33px; }
  .website { top: 537px; }
</style>
</head>
<body>
  <main class="card">
    <section class="brand">
      <div class="brand-square" aria-hidden="true"></div>
      <h1 class="brand-name">VELMONT</h1>
      <p class="brand-sub">REALTORS</p>
    </section>

    <div class="divider" aria-hidden="true"></div>

    <section class="contact">
      <h2 class="contact-name">HOWARD PRISK</h2>
      <p class="contact-title">BROKER</p>
      <p class="detail phone"><span class="detail-label">Phone:</span>818-555-0142</p>
      <p class="detail fax"><span class="detail-label">Fax:</span>626-555-0187</p>
      <p class="detail email">hprisk@velmontrealtors.com</p>
      <p class="detail license">CA BRE 02481736</p>
      <p class="detail address">4153 Marlow Ave. #226<br>La Crescenta, CA 91207</p>
      <p class="detail website">www.velmontrealtors.com</p>
    </section>
  </main>
</body>
</html>
```